Einladungskarten für Der Helle Bogen
Designer hat mehrere Vorschläge entwickelt und Änderungen super schnell umgesetzt. Wir waren sehr zufrieden und freuen uns auf unsere diesjährige Einladungskarte.
Zielgruppe
Wir sind ein Tochterunternehmen von Harting Verlag. Wir sind 'Der Helle Bogen' , Holding der Radio Stationen/Beteiligungen und möchten alle Geschäftsführer/innen der Beteiligungen, einige Politiker und Medienräte zu einem Event einladen.
Aufgabenstellung
Wir hätten gerne eine quadratische Karte.
Das Event heißt 'Ortsabend 2023'
Termin 03.07.2023 um 19 Uhr
Anmeldung bis spätestens 23.06.2022 an events@heller-bogen.de
Diese Karte gilt als Eintrittskarte
Adresse: KAIHALLE, Lindenweg 52, 90461 Nürnberg
Dresscode: Business Casual
Firmenfarben: Blau: RGB 23/110/182 und Grau: RGB 134/135/135
Firmenschriftart: Century Gothic

```html
<!DOCTYPE html>
<html lang="de">
<head>
<meta charset="utf-8">
<title>Ortsabend 2023 – Einladung</title>
<link rel="stylesheet" href="https://fonts.googleapis.com/css2?family=Questrial&family=PT+Serif:ital,wght@1,700&display=swap">
<style>
  :root {
    --brand-blue: rgb(23, 110, 182);
    --brand-grey: rgb(134, 135, 135);
    --text-grey: #6f7070;
    --card: #f7f7f7;
    --backdrop: #d9d9d9;
    --rule: #bdbdbd;
  }
  * { margin: 0; padding: 0; box-sizing: border-box; }
  html, body {
    width: 1200px;
    height: 1071px;
    overflow: hidden;
    background: var(--backdrop);
    font-family: 'Questrial', 'Century Gothic', sans-serif;
  }
  .invitation-card {
    position: absolute;
    left: 230px;
    top: 150px;
    width: 740px;
    height: 760px;
    background: var(--card);
    box-shadow: 0 10px 30px rgba(0, 0, 0, 0.12);
  }
  .card-frame {
    position: absolute;
    inset: 22px;
    border: 2px dashed var(--rule);
    display: flex;
    flex-direction: column;
    align-items: center;
    text-align: center;
    padding-top: 62px;
  }
  .event-mark {
    display: flex;
    align-items: center;
    gap: 14px;
    font-size: 46px;
    letter-spacing: 1px;
    color: var(--brand-blue);
    line-height: 1;
  }
  .event-mark-dot {
    width: 34px;
    height: 34px;
    border-radius: 50%;
    background: var(--brand-grey);
  }
  .event-title {
    margin-top: 10px;
    font-size: 56px;
    font-weight: 400;
    color: var(--brand-blue);
    line-height: 1.1;
  }
  .event-date {
    margin-top: 36px;
    display: flex;
    align-items: center;
    gap: 12px;
    font-size: 28px;
    color: var(--brand-blue);
  }
  .event-date .play-icon { width: 26px; height: 28px; }
  .event-date em {
    font-family: 'PT Serif', Georgia, serif;
    font-weight: 700;
    font-style: italic;
  }
  .registration {
    margin-top: 28px;
    font-size: 25px;
    color: var(--text-grey);
    line-height: 1.3;
  }
  .registration-mail {
    display: block;
    font-size: 27px;
    letter-spacing: 1px;
    color: var(--text-grey);
  }
  .ticket-note {
    margin-top: 20px;
    font-size: 25px;
    letter-spacing: 0.5px;
    color: var(--text-grey);
  }
  .host-name {
    margin-top: 52px;
    display: flex;
    align-items: center;
    gap: 10px;
    font-size: 24px;
    letter-spacing: 1px;
    color: var(--brand-grey);
  }
  .host-square {
    width: 14px;
    height: 14px;
    background: var(--brand-blue);
  }
  .venue {
    margin-top: 36px;
    display: flex;
    align-items: center;
    gap: 8px;
    font-size: 19px;
    color: var(--text-grey);
  }
  .venue .pin-icon { width: 16px; height: 22px; }
  .dresscode {
    margin-top: 8px;
    font-size: 16px;
    color: var(--brand-grey);
  }
</style>
</head>
<body>
  <article class="invitation-card">
    <div class="card-frame">
      <div class="event-mark">
        <span>ORTSABEND</span>
        <span class="event-mark-dot"></span>
      </div>
      <h1 class="event-title">Ortsabend 2023</h1>

      <p class="event-date">
        <svg class="play-icon" viewBox="0 0 26 28" aria-hidden="true"><polygon points="0,0 26,14 0,28" fill="rgb(23,110,182)"/></svg>
        <span>Termin <em>03.07.2023</em> um <em>19 Uhr</em></span>
      </p>

      <p class="registration">
        Anmeldung bis spätestens 23.06.2023 an
        <span class="registration-mail">events@heller-bogen.de</span>
      </p>

      <p class="ticket-note">Diese Karte gilt als Eintrittskarte</p>

      <div class="host-name">
        <span>DER HELLE BOGEN</span>
        <span class="host-square"></span>
      </div>

      <p class="venue">
        <svg class="pin-icon" viewBox="0 0 16 22" aria-hidden="true">
          <path d="M8 0C3.6 0 0 3.5 0 7.8 0 13.5 8 22 8 22s8-8.5 8-14.2C16 3.5 12.4 0 8 0zm0 11a3.2 3.2 0 1 1 0-6.4A3.2 3.2 0 0 1 8 11z" fill="#6f7070"/>
        </svg>
        <span>KAIHALLE, Lindenweg 52, 90461 Nürnberg</span>
      </p>
      <p class="dresscode">Dresscode: Business Casual</p>
    </div>
  </article>
</body>
</html>
```